Self Help / Psychology Ebook Cover Design

Looking for a design based on the concept of the I AM (You) placed at the centre of a radar screen. The design should communicate the concept of using our built in human radar coupled with intuition to navigate to a new life that we are actively creating. <br/>The image attached is to give a visual brief / idea / concept. BUT you are NOT restricted to this. <br/>The RADAR concept is featured in the book and a key element to what they book sets out to achieve.<br/>The TITLE of the book will need to be on the cover.<br/>STEPS TOWARD SHAPING A FUTURE WORTH CHOOSING.<br/><br/>Author Name to be at the foot of the book similar to the design on one of my earlier books. You can view that book cover at.<br/>https://derekvallow.example/<br/>
Target Market(s)
Self help / psychology / success
Colors
Designer to choose colors to be used in the design.
Look and feel

```html
<!DOCTYPE html>
<html lang="en">
<head>
<meta charset="utf-8">
<title>Steps Toward Shaping a Future Worth Choosing — Derek Vallow</title>
<link rel="stylesheet" href="https://fonts.googleapis.com/css2?family=Montserrat:wght@700&family=Oswald:wght@300;700&display=swap">
<style>
  :root {
    --sky-top: #1e6fa8;
    --sky-mid: #2f8fc4;
    --night: #05080b;
    --sun: #fff3a6;
    --sun-glow: #f3c43a;
    --sea: #2d7a78;
    --sea-deep: #0d2a2d;
    --gold: #ffd21a;
    --gold-deep: #f2a900;
    --white: #ffffff;
    --ring: rgba(255, 255, 255, 0.35);
  }
  html, body {
    margin: 0;
    padding: 0;
    width: 800px;
    height: 1200px;
    overflow: hidden;
    background: var(--night);
  }
  .cover {
    position: relative;
    width: 800px;
    height: 1200px;
    overflow: hidden;
  }
  .city-backdrop {
    position: absolute;
    inset: 0;
    background: linear-gradient(180deg, var(--sky-top) 0%, var(--sky-mid) 18%, #1b4f73 34%, #0b1a24 55%, var(--night) 75%);
  }
  .radar-scene {
    position: absolute;
    left: 11px;
    top: 278px;
    width: 778px;
    height: 778px;
    border-radius: 50%;
    background:
      radial-gradient(circle at 52% 30%, var(--sun) 0%, var(--sun-glow) 14%, #c9b44c 30%, transparent 48%),
      linear-gradient(180deg, #e8d77a 0%, #d9c85a 28%, #8cab6a 42%, var(--sea) 58%, #1f5a5a 75%, var(--sea-deep) 100%);
    overflow: hidden;
  }
  .radar-rings {
    position: absolute;
    left: 11px;
    top: 278px;
    width: 778px;
    height: 778px;
  }
  .author {
    position: absolute;
    top: 36px;
    left: 0;
    width: 800px;
    margin: 0;
    text-align: center;
    font-family: "Montserrat", sans-serif;
    font-weight: 700;
    font-size: 58px;
    letter-spacing: 12px;
    color: var(--gold);
  }
  .title {
    position: absolute;
    left: 0;
    top: 630px;
    width: 800px;
    margin: 0;
    text-align: center;
    font-family: "Oswald", sans-serif;
    text-transform: uppercase;
  }
  .title span { display: block; }
  .title .light {
    font-weight: 300;
    font-size: 58px;
    line-height: 62px;
    color: var(--white);
  }
  .title .key {
    font-weight: 700;
    font-size: 150px;
    line-height: 150px;
    background: linear-gradient(180deg, var(--gold) 40%, var(--gold-deep) 100%);
    -webkit-background-clip: text;
    background-clip: text;
    color: transparent;
  }
  .title .key-first { margin: 4px 0 8px; }
  .title .key-last { margin-top: 8px; }
  .arrow-right, .arrow-down {
    position: absolute;
  }
  .arrow-right { left: 612px; top: 770px; width: 150px; height: 40px; }
  .arrow-down { left: 380px; top: 1120px; width: 40px; height: 80px; }
</style>
</head>
<body>
<main class="cover">
  <div class="city-backdrop" role="img" aria-label="Blue-toned city skyline photograph fading to black"></div>
  <div class="radar-scene" role="img" aria-label="Photograph of a runner on a beach at sunrise, birds in the sky, seen through a round radar screen"></div>
  <svg class="radar-rings" viewBox="0 0 778 778" aria-hidden="true">
    <g fill="none" stroke="var(--ring)" stroke-width="2">
      <circle cx="389" cy="389" r="80"/>
      <circle cx="389" cy="389" r="160"/>
      <circle cx="389" cy="389" r="240"/>
      <circle cx="389" cy="389" r="320"/>
    </g>
  </svg>

  <h2 class="author">DEREK VALLOW</h2>

  <h1 class="title">
    <span class="light">Steps Toward</span>
    <span class="key key-first">Shaping</span>
    <span class="light">A Future</span>
    <span class="light">Worth</span>
    <span class="key key-last">Choosing</span>
  </h1>

  <svg class="arrow-right" viewBox="0 0 150 40" aria-hidden="true">
    <rect x="0" y="16" width="125" height="8" fill="var(--gold-deep)"/>
    <polygon points="122,4 150,20 122,36" fill="var(--gold-deep)"/>
  </svg>
  <svg class="arrow-down" viewBox="0 0 40 80" aria-hidden="true">
    <rect x="16" y="0" width="8" height="55" fill="var(--gold-deep)"/>
    <polygon points="4,52 36,52 20,80" fill="var(--gold-deep)"/>
  </svg>
</main>
</body>
</html>
```